Design Memorial Booklet for our Mum

We have put together 4,400 words with 57 photos of our mum who passed away recently. Due to covid restrictions, we were unable to hold a funeral with all the family and friends so we planning to send an A5 booklet out to them to celebrate her life instead.
The booklet should be beautiful and celebrate her life focussing on the vibrant photos of her.
All text and low resolution photos are in this document: Quillora https://pages.quillora.example/doc/d/7kRtPmw2XzLq9VbNcYhT4eUaGs8FjDoK3iWyEr6Hnv/edit?usp=sharing

Photos: https://vault.quillora.example/vault/folders/9pXcVn4k2Ls7Tb5qWmRz3-yHdJf82Ku?usp=sharing

We can give access to a folder with high resolution photos for the final print file.
Booklet will be printed in A5 (A4 folded in half and bound) so final format will need to be in page multiples of 4.

Output file type: pdf - ready for printing + raw file (InDesign or similar)

Update: For this competition please can you submit the cover page plus 1-2 inside pages to show us the style. Based on this we will select a winner to complete the work.

We are looking for a fast turnaround on this project.

Thanks for your patience for us new users of this.

Target Market(s)

Friends and Family

Industry/Entity Type

Personal Project

Requirements
Must have
• Look professional. Let the beautiful photos be the feature. Creative but respectful.

```html
<!DOCTYPE html>
<html lang="en">
<head>
<meta charset="utf-8">
<title>A Celebration of Nana Dove's Life</title>
<link href="https://fonts.googleapis.com/css2?family=EB+Garamond:wght@400&family=Pinyon+Script&display=swap" rel="stylesheet">
<style>
  :root {
    --ink: #7a665e;
    --title: #9a8780;
    --gold: #d4a640;
    --gold-deep: #b8702c;
    --gold-soft: #e9c983;
    --page-top: #fdfbfb;
    --page-bottom: #fae2e9;
  }
  * { margin: 0; padding: 0; box-sizing: border-box; }
  html, body { width: 846px; height: 1200px; overflow: hidden; }
  body { background: var(--page-top); }
  .page {
    position: relative;
    width: 846px;
    height: 1200px;
    overflow: hidden;
    background: linear-gradient(180deg, var(--page-top) 0%, var(--page-top) 42%, #fcf0f3 68%, var(--page-bottom) 100%);
    font-family: "EB Garamond", Garamond, serif;
    color: var(--ink);
  }
  .rose-ornament {
    position: absolute;
    left: 552px; top: -20px;
    width: 310px; height: 330px;
    border-radius: 48% 40% 52% 46%;
    background: radial-gradient(ellipse at 60% 38%, rgba(222,176,84,0.38) 0%, rgba(214,160,70,0.24) 38%, rgba(200,130,60,0.12) 62%, rgba(200,130,60,0) 80%);
  }
  .title {
    position: absolute;
    left: 0; top: 0;
    font-family: "Pinyon Script", cursive;
    font-weight: 400;
    color: var(--title);
    line-height: 1;
  }
  .title-main { position: absolute; left: 56px; top: 22px; font-size: 84px; white-space: nowrap; }
  .title-sub { position: absolute; left: 72px; top: 104px; font-size: 62px; white-space: nowrap; }
  .section-heading {
    position: absolute;
    font-family: "Pinyon Script", cursive;
    font-weight: 400;
    font-size: 28px;
    color: var(--ink);
    line-height: 1;
    white-space: nowrap;
  }
  .body-text { position: absolute; font-size: 18.5px; line-height: 21.8px; }
  .body-text p + p { margin-top: 5px; }
  .parents-heading { left: 57px; top: 214px; }
  .parents-text { left: 57px; top: 250px; width: 314px; }
  .childhood-heading { left: 284px; top: 630px; }
  .childhood-text { left: 284px; top: 667px; width: 492px; }
  .photo { position: absolute; }
  .photo-family-porch {
    left: 402px; top: 209px; width: 387px; height: 398px;
    border: 4px solid var(--gold);
    border-image: linear-gradient(135deg, var(--gold-deep), #f0cf6e, var(--gold-deep)) 1;
    background: linear-gradient(165deg, #8a8580 0%, #b5b0aa 35%, #7b7671 70%, #55514d 100%);
    box-shadow: 0 2px 6px rgba(0,0,0,0.2);
  }
  .photo-framed {
    border: 4px solid #fff;
    box-shadow: 0 2px 5px rgba(0,0,0,0.22);
  }
  .photo-young-girl {
    left: 56px; top: 635px; width: 199px; height: 232px;
    background: linear-gradient(160deg, #c2bfbb 0%, #8e8a86 55%, #6c6864 100%);
  }
  .photo-garden-group {
    left: 60px; top: 880px; width: 377px; height: 258px;
    transform: rotate(-2deg);
    background: linear-gradient(120deg, #d9913f 0%, #a88a5e 22%, #9a6f6e 45%, #c9486e 62%, #8a9a78 82%, #6c6a58 100%);
  }
  .photo-birthday-party {
    left: 468px; top: 810px; width: 318px; height: 330px;
    transform: rotate(2deg);
    background: linear-gradient(175deg, #b9b5b0 0%, #7e7a76 45%, #55524f 100%);
  }
</style>
</head>
<body>
<main class="page">
  <div class="rose-ornament" role="img" aria-label="Gold line-art rose decoration"></div>

  <h1 class="title">
    <span class="title-main">A Celebration</span>
    <span class="title-sub">of Nana Dove’s Life</span>
  </h1>

  <h2 class="section-heading parents-heading">Parents to Rhodesia</h2>
  <div class="body-text parents-text">
    <p>Born in Goa, Elena’s father, Tomas Aurelio, was looking for a better life, with opportunities to bring up a family in a better environment.</p>
    <p>He took a boat with some mates to East Africa traveling inland from Beira to Salisbury, Southern Rhodesia and found a land of opportunity with space, good soil and magnificent weather. Tomas was offered work as an apprentice dressmaker. He returned to Goa, married Rosa Beatriz and took her on a wild adventure across the Indian Ocean to make a new life, along with their four poster bed. Tomas was a skilled tailor and quickly established a business along with the other new immigrant Goan families.</p>
  </div>

  <div class="photo photo-family-porch" role="img" aria-label="Black and white photo of the family standing on the porch steps of their home"></div>

  <div class="photo photo-framed photo-young-girl" role="img" aria-label="Black and white photo of Elena as a smiling little girl among blossoms"></div>

  <h2 class="section-heading childhood-heading">Childhood in Rhodesia</h2>
  <div class="body-text childhood-text">
    <p>Elena’s parents built a home in Ardbennie which was renowned for hospitality, sharing all that they had with friends and neighbours.</p>
    <p>Rosa Beatriz devoted the next 20 years welcoming eight little Almeida babies: Paul, Frank, Lucia, Henry, Marino, Alberto, Ray and the last little rascal named Elena.</p>
  </div>

  <div class="photo photo-framed photo-garden-group" role="img" aria-label="Colour photo of the family gathered in a garden beside red hot poker flowers"></div>
  <div class="photo photo-framed photo-birthday-party" role="img" aria-label="Black and white photo of family and friends gathered around a birthday cake"></div>
</main>
</body>
</html>
```